Law Firm Business Cards & Stationary
Firm Wide Cards, Letterhead, Envelopes
Professional
Dara Wells Fenwick, Esq.
Attorney at Law
815 Brambleton Hollow Road
Suite 340
Westerville, Ohio 43097
dara@pmfenwicklegal.com
We need a generic business card for all attorney's in the firm. The design should leave the specific info blank and therefore have the ability to be modified for printing each attorney's cards/stationary. The stationary should have the firm's name and address, and should also have the ability the be modified so each attorney can add his/her own phone line.

```html
<!DOCTYPE html>
<html lang="en">
<head>
<meta charset="utf-8">
<title>Fenwick, Fenwick &amp; Associates — Stationery Set</title>
<link rel="stylesheet" href="https://fonts.googleapis.com/css2?family=Cinzel:wght@500&family=Open+Sans:wght@400&display=swap">
<style>
  :root {
    --bg-center: #a4a4a4;
    --bg-edge: #6f6f6f;
    --paper: #ffffff;
    --green: #1e6d3a;
    --green-dark: #0d4322;
    --green-light: #3f9a5c;
    --ink: #3a3a3a;
    --ink-soft: #6a6a6a;
    --mark-faint: #e9ecea;
  }
  * { box-sizing: border-box; margin: 0; padding: 0; }
  html, body { width: 1200px; height: 626px; overflow: hidden; }
  body {
    position: relative;
    background: radial-gradient(ellipse at 50% 45%, var(--bg-center) 0%, var(--bg-edge) 100%);
    font-family: "Open Sans", Arial, sans-serif;
    color: var(--ink);
  }
  .sheet {
    position: absolute;
    background: var(--paper);
    box-shadow: 0 2px 6px rgba(0,0,0,0.28);
    overflow: hidden;
  }

  /* firm name block */
  .firm { display: flex; flex-direction: column; align-items: center; }
  .firm-square { background: var(--green-dark); }
  .firm-name {
    font-family: "Cinzel", "Times New Roman", serif;
    font-weight: 500;
    color: var(--ink);
    text-align: center;
    line-height: 1.1;
    letter-spacing: 0.02em;
  }

  .bar-top, .bar-bottom {
    position: absolute; left: 0; right: 0;
    background: linear-gradient(90deg, var(--green-dark), var(--green), var(--green-dark));
  }
  .bar-top { top: 0; }
  .bar-bottom { bottom: 0; }

  .footer-line {
    position: absolute; left: 0; right: 0;
    text-align: center;
    font-size: 4.6px;
    color: var(--ink-soft);
    white-space: nowrap;
  }

  /* business card front */
  .card-front { left: 34px; top: 264px; width: 187px; height: 101px; }
  .card-front .firm { position: absolute; inset: 0; justify-content: center; gap: 3px; }
  .card-front .firm-square { width: 20px; height: 20px; }
  .card-front .firm-name { font-size: 5.5px; }

  /* business card back */
  .card-back { left: 34px; top: 377px; width: 187px; height: 101px; }
  .card-back .bar-bottom { height: 5px; }
  .card-back .firm { position: absolute; left: 10px; top: 9px; align-items: flex-start; flex-direction: row; gap: 4px; }
  .card-back .firm-square { width: 13px; height: 13px; }
  .card-back .firm-name { font-size: 4.6px; text-align: left; }
  .card-details { position: absolute; left: 56px; top: 36px; font-size: 4.4px; line-height: 1.35; color: var(--ink-soft); }
  .card-contact { position: absolute; left: 56px; top: 66px; font-size: 4.2px; line-height: 1.35; color: var(--ink-soft); }
  .person-name { color: var(--ink); }

  /* letterhead */
  .letterhead { left: 233px; top: 19px; width: 427px; height: 574px; }
  .letterhead .bar-top { height: 9px; }
  .letterhead .bar-bottom { height: 8px; }
  .letterhead .firm.header { position: absolute; top: 30px; left: 0; right: 0; gap: 3px; }
  .letterhead .firm-square { width: 22px; height: 22px; }
  .letterhead .firm-name { font-size: 9px; }
  .backdrop-mark {
    position: absolute; left: 143px; top: 206px; width: 140px; height: 140px;
    border: 5px solid var(--mark-faint);
    display: flex; align-items: center; justify-content: center;
  }
  .backdrop-mark span {
    font-family: "Cinzel", "Times New Roman", serif;
    font-weight: 500; font-size: 14px; color: var(--mark-faint); text-align: center; line-height: 1.2;
  }
  .letterhead .footer-line { bottom: 24px; }

  /* envelope back */
  .envelope-back { left: 679px; top: 79px; width: 485px; height: 233px; }
  .envelope-back svg { display: block; }

  /* envelope front */
  .envelope-front { left: 679px; top: 338px; width: 485px; height: 250px; }
  .envelope-front .bar-top { height: 9px; }
  .envelope-front .bar-bottom { height: 9px; }
  .envelope-front .firm { position: absolute; top: 36px; left: 0; right: 0; gap: 3px; }
  .envelope-front .firm-square { width: 20px; height: 20px; }
  .envelope-front .firm-name { font-size: 8.5px; }
  .envelope-front .footer-line { bottom: 24px; }
</style>
</head>
<body>

  <section class="sheet card-front" aria-label="Business card front">
    <div class="firm">
      <div class="firm-square"></div>
      <div class="firm-name">Fenwick, Fenwick<br>&amp; Associates, LLC</div>
    </div>
  </section>

  <section class="sheet card-back" aria-label="Business card back">
    <div class="firm">
      <div class="firm-square"></div>
      <div class="firm-name">Fenwick, Fenwick<br>&amp; Associates, LLC</div>
    </div>
    <div class="card-details">
      <div class="person-name">Dara Wells Fenwick, Esq.</div>
      <div>Attorney at Law</div>
      <div>815 Brambleton Hollow Road</div>
      <div>Suite 340</div>
      <div>Westerville, Ohio 43097</div>
    </div>
    <div class="card-contact">
      <div>dara@pmfenwicklegal.com</div>
      <div>T 614.555.0142 F 614.555.0143</div>
    </div>
    <div class="bar-bottom"></div>
  </section>

  <section class="sheet letterhead" aria-label="Letterhead">
    <div class="bar-top"></div>
    <div class="firm header">
      <div class="firm-square"></div>
      <div class="firm-name">Fenwick, Fenwick<br>&amp; Associates, LLC</div>
    </div>
    <div class="backdrop-mark"><span>Fenwick, Fenwick<br>&amp; Associates</span></div>
    <p class="footer-line">T 614.555.0142 | F 614.555.0143 | dara@pmfenwicklegal.com | 815 Brambleton Hollow Road, Suite 340, Westerville, Ohio 43097</p>
    <div class="bar-bottom"></div>
  </section>

  <section class="sheet envelope-back" aria-label="Envelope back with flap">
    <svg width="485" height="233" viewBox="0 0 485 233">
      <defs>
        <radialGradient id="flapFill" cx="50%" cy="20%" r="75%">
          <stop offset="0%" stop-color="var(--green-light)"/>
          <stop offset="55%" stop-color="var(--green)"/>
          <stop offset="100%" stop-color="var(--green-dark)"/>
        </radialGradient>
      </defs>
      <rect width="485" height="233" fill="var(--paper)"/>
      <path d="M0 0 H485 V118 L242 150 L0 118 Z" fill="url(#flapFill)"/>
      <path d="M0 233 L242 150 L485 233" fill="none" stroke="#e2e2e2" stroke-width="1"/>
    </svg>
  </section>

  <section class="sheet envelope-front" aria-label="Envelope front">
    <div class="bar-top"></div>
    <div class="firm">
      <div class="firm-square"></div>
      <div class="firm-name">Fenwick, Fenwick<br>&amp; Associates, LLC</div>
    </div>
    <p class="footer-line">T 614.555.0142 | F 614.555.0143 | dara@pmfenwicklegal.com | 815 Brambleton Hollow Road, Suite 340, Westerville, Ohio 43097</p>
    <div class="bar-bottom"></div>
  </section>

</body>
</html>
```